Broschüre für Gleichstellungsstelle einer kommunalen Stadtverwaltung
Zielgruppe
Wir sind die Gleichstellungsstelle einer kommunalen Stadtverwaltung (Einwohner*innen ca. 74.500) und richten uns mit unserer Arbeit grundsätzlich an alle Menschen.
Wir wollen eine Broschüre zum Handlungsleitfaden für die geschlechtergerechte Sprache bei der Stadt erstellen. Dieser soll an die Beschäftigten als Unterstützung verteilt werden.
Aufgabenstellung
- Broschüre mit Wire-O-Bindung, Druckformat 14,8 cm x 14,8 cm, Endformat 15,0 x 15,0 cm
- Spiralbindung an der Kopfseite
- doppelseitiges Deckblatt und Rückseite
- 16 Seiten Inhalt, wobei lediglich die Vorderseiten Text enthalten
- Schriftart (optimal Avenir Next, alternativ Arial) und Farbschema laut Corporate Design
- Der Text ist vorgegeben, die Gestaltung ist im Rahmen des Corporate Designs frei
Es soll eine ansprechende Broschüre gestaltet werden, welche die Leser*innen zum Blättern einlädt. Das bedeutet, dass alle Seiten (Deckblatt, Inhaltsseiten und Rückseiten) bei der Gestaltung berücksichtigt werden müssen.
Am Ende soll neben den üblichen Dateien auch eine fertige Druckdatei (siehe Datenblatt) zur Verfügung gestellt werden. Dabei ist zu beachten, dass die Spiralbindung des fertigen Produkts an der Kopfseite sein soll.

```html
<!DOCTYPE html>
<html lang="de">
<head>
<meta charset="utf-8">
<title>How to Gender – Broschüre</title>
<link rel="stylesheet" href="https://fonts.googleapis.com/css2?family=Montserrat:wght@600&family=Nunito+Sans:wght@500&display=swap">
<style>
  :root {
    --bg: #d8e1e0;
    --ink: #0b5a4f;
    --tone-orange: #f39a2b;
    --tone-red: #e8453a;
    --tone-teal: #2aa59a;
    --tone-blue: #2a4fa8;
    --tone-pink: #f07a86;
    --tone-paper: #f3f5f4;
  }
  * { margin: 0; padding: 0; box-sizing: border-box; }
  html, body { width: 1200px; height: 1200px; overflow: hidden; }
  body { background: var(--bg); }
  .cover {
    position: relative;
    width: 1200px;
    height: 1200px;
    background: var(--bg);
  }
  .cover-title {
    position: absolute;
    top: 112px;
    left: 0;
    width: 100%;
    text-align: center;
    font-family: "Montserrat", "Avenir Next", Arial, sans-serif;
    font-weight: 600;
    font-size: 108px;
    line-height: 1;
    letter-spacing: 2px;
    color: var(--ink);
  }
  .cover-subtitle {
    position: absolute;
    top: 224px;
    left: 0;
    width: 100%;
    text-align: center;
    font-family: "Nunito Sans", "Avenir Next", Arial, sans-serif;
    font-weight: 500;
    font-size: 29px;
    line-height: 1.2;
    color: var(--ink);
  }
  .cover-artwork {
    position: absolute;
    left: 222px;
    top: 345px;
    width: 790px;
    height: 785px;
  }
</style>
</head>
<body>
  <main class="cover">
    <h1 class="cover-title">HOW TO GENDER</h1>
    <p class="cover-subtitle">Tipps für die Verwendung einer geschlechtergerechten Sprache</p>
    <svg class="cover-artwork" viewBox="0 0 790 785" role="img" aria-label="Farbenfrohe geometrische Illustration mehrerer menschlicher Kopfprofile in Orange, Rot, Türkis, Blau und Rosa, umgeben von kleinen Formen und Punkten">
      <defs>
        <linearGradient id="artwork-tones" x1="0" y1="0" x2="1" y2="1">
          <stop offset="0" stop-color="var(--tone-orange)"/>
          <stop offset="0.35" stop-color="var(--tone-red)"/>
          <stop offset="0.6" stop-color="var(--tone-pink)"/>
          <stop offset="0.8" stop-color="var(--tone-teal)"/>
          <stop offset="1" stop-color="var(--tone-blue)"/>
        </linearGradient>
      </defs>
      <path d="M40 785 V300 C40 130 190 10 395 10 C600 10 750 130 750 300 V785 Z" fill="url(#artwork-tones)" opacity="0.85"/>
      <line x1="0" y1="783" x2="790" y2="783" stroke="var(--tone-paper)" stroke-width="3"/>
    </svg>
  </main>
</body>
</html>
```